Service Menu refresh 2018 Update of menu pricing

We currently have service menus as attached. We will be updating our look via our homepage image, our service menu and our in-house beverage and treatment menu.
We are a natural and sustainable hair salon group and moving more towards head spa which consists of treatments, beauty, tanning as well as your traditional hair services. Our imagery needs to reflect our efforts in spa treatments in the hair and scalp area and use natural materials and colours reflecting sustainability.
Velin is the brand we stock and promote.

Target Market(s)

Men or women interesting in personal maintenance with natural and organic products and using sustainable practises

Industry/Entity Type

Hair And Beauty

Font styles to use
Sans Serif
Other font styles liked:
• Arial or Helvetica

Colors
9acb3c
abd037
cadf82
ffffff

Requirements
Must have
• Name on the front cover, locations on back cover
Nice to have
• Prestige feel, reflect male and female clients
Should not have
• Bold artificial writing or any type of cartoon images.
• Same images as existing menu.

```html
<!DOCTYPE html>
<html lang="en">
<head>
<meta charset="utf-8">
<title>Greenleaf Hair Studios – Service Menu Covers</title>
<link href="https://fonts.googleapis.com/css2?family=Arimo:wght@400;700&family=Tinos:ital,wght@1,700&display=swap" rel="stylesheet">
<style>
  :root{
    --leaf:#9acb3c;
    --lime:#abd037;
    --pale:#cadf82;
    --white:#ffffff;
    --forest:#3f9a2f;
    --deep:#2e7d24;
    --ink:#1f1f1f;
    --stage:#ece6e2;
  }
  *{box-sizing:border-box;margin:0;padding:0}
  html,body{width:1200px;height:824px;overflow:hidden;background:var(--stage)}
  body{font-family:"Arimo",Arial,sans-serif;color:var(--ink)}
  .spread{position:absolute;left:48px;top:22px;width:1104px;height:780px;display:flex;box-shadow:0 10px 30px rgba(0,0,0,.18)}
  .page{position:relative;width:552px;height:780px;overflow:hidden}
  .page svg.layer{position:absolute;inset:0;width:552px;height:780px}

  /* back cover */
  .back{background:linear-gradient(180deg,#bfe08a 0%,#e4f1cf 45%,#f3f8ea 70%,var(--white) 100%)}
  .quote{position:absolute;left:44px;top:130px;width:470px;font-family:"Tinos","Times New Roman",serif;font-style:italic;font-weight:700;font-size:21px;line-height:1.25;color:var(--ink)}
  .locations{position:absolute;left:44px;top:222px;width:480px}
  .locations h2{font-size:19px;font-weight:700;color:var(--forest);margin-bottom:12px}
  .location{margin-bottom:12px;font-size:12.5px;line-height:1.3}
  .location:last-child{margin-bottom:0}
  .location h3{font-size:13px;font-weight:700;color:var(--forest);text-transform:uppercase;letter-spacing:.3px}
  .web{position:absolute;font-size:14px;font-weight:700;color:var(--white);letter-spacing:.3px}
  .back .web{left:44px;bottom:30px}

  /* front cover */
  .front{background:linear-gradient(180deg,var(--white) 0%,var(--white) 18%,#eef6e2 55%,#dcefc2 80%)}
  .brand{position:absolute;right:48px;top:52px;display:flex;align-items:center;gap:12px}
  .brand-dot{width:34px;height:34px;border-radius:50%;background:var(--leaf)}
  .brand-name{font-size:27px;font-weight:400;color:var(--ink);letter-spacing:.2px}
  .front .web{right:40px;bottom:34px}
</style>
</head>
<body>
<main class="spread">

  <section class="page back" aria-label="Back cover">
    <svg class="layer" viewBox="0 0 552 780">
      <defs>
        <radialGradient id="canopy" cx="70%" cy="20%" r="80%">
          <stop offset="0" stop-color="#e9f5c8"/>
          <stop offset=".5" stop-color="#9fd067"/>
          <stop offset="1" stop-color="#6fb544" stop-opacity="0"/>
        </radialGradient>
      </defs>
      <rect role="img" aria-label="Sunlit canopy of green leaves" x="0" y="0" width="552" height="215" fill="url(#canopy)"/>
      <path d="M0 692 C150 676 330 664 552 640 L552 780 L0 780 Z" fill="var(--lime)"/>
      <path d="M0 700 C160 684 330 672 552 648" fill="none" stroke="#e8ef6a" stroke-width="5"/>
      <path d="M0 712 C170 696 340 684 552 662 L552 780 L0 780 Z" fill="var(--leaf)"/>
      <path d="M0 728 C180 712 350 700 552 682 L552 780 L0 780 Z" fill="#6fb73d"/>
    </svg>

    <p class="quote">“Living a more natural and organic life is a philosophy not just a product certification”</p>

    <div class="locations">
      <h2>Our Locations</h2>
      <div class="location">
        <h3>Ferncliff</h3>
        <p>Shop 104 Parkway Ferncliff, Brook Rd, Ferncliff<br>+61 (07) 3100 2741<br>ferncliff@greenleafhairstudios.com.au</p>
      </div>
      <div class="location">
        <h3>Mossvale</h3>
        <p>Shop 212 Parkway Mossvale, Linden Road, Mossvale<br>+61 (07) 3100 2742<br>mossvale@greenleafhairstudios.com.au</p>
      </div>
      <div class="location">
        <h3>Willowbrook</h3>
        <p>Shop 3040 Willowbrook Shopping Centre, Tallis Rd Willowbrook.<br>+61 (07) 3100 2743<br>willowbrook@greenleafhairstudios.com.au</p>
      </div>
      <div class="location">
        <h3>Lakeshore</h3>
        <p>Shop 1190 Parkway Lakeshore, Harbour St, Lakeshore<br>+61 (07) 3100 2744<br>lakeshore@greenleafhairstudios.com.au</p>
      </div>
      <div class="location">
        <h3>Eastgate General Hospital</h3>
        <p>Wattle St, Eastgate QLD 4099<br>+61 (07) 3100 2745<br>eastgate@greenleafhairstudios.com.au</p>
      </div>
    </div>

    <p class="web">www.greenleafhairstudios.com.au</p>
  </section>

  <section class="page front" aria-label="Front cover">
    <svg class="layer" viewBox="0 0 552 780">
      <defs>
        <linearGradient id="portrait" x1="0" y1="0" x2="1" y2="1">
          <stop offset="0" stop-color="#9aa19a"/>
          <stop offset=".45" stop-color="#6e7a5c"/>
          <stop offset="1" stop-color="#3f5a2e"/>
        </linearGradient>
        <linearGradient id="treatment" x1="0" y1="0" x2="1" y2="1">
          <stop offset="0" stop-color="#e8e4dc"/>
          <stop offset="1" stop-color="#a7b5c6"/>
        </linearGradient>
        <linearGradient id="products" x1="0" y1="0" x2="1" y2="1">
          <stop offset="0" stop-color="#f4efe8"/>
          <stop offset="1" stop-color="#d7b7a8"/>
        </linearGradient>
      </defs>
      <path d="M24 135 L552 135 L552 420 C500 470 430 500 340 505 C230 510 150 470 95 390 C55 330 30 250 24 135 Z" fill="var(--deep)"/>
      <path role="img" aria-label="Photo of a woman in a sun hat among greenhouse plants" d="M34 140 L552 140 L552 410 C495 460 425 490 340 494 C235 498 158 460 105 384 C66 326 42 250 34 140 Z" fill="url(#portrait)"/>
      <circle role="img" aria-label="Photo of a stylist preparing a natural hair treatment" cx="200" cy="445" r="62" fill="url(#treatment)" stroke="#c9c9c9" stroke-width="4"/>
      <circle role="img" aria-label="Photo of natural treatment ingredients and strawberries on a table" cx="306" cy="478" r="52" fill="url(#products)" stroke="#c9c9c9" stroke-width="4"/>
      <path d="M0 560 C180 590 360 560 552 510 L552 780 L0 780 Z" fill="var(--pale)"/>
      <path d="M0 575 C190 605 370 575 552 525" fill="none" stroke="#e8ef6a" stroke-width="6"/>
      <path d="M0 600 C200 630 380 600 552 555 L552 780 L0 780 Z" fill="var(--leaf)"/>
      <path d="M0 640 C200 665 390 640 552 600 L552 780 L0 780 Z" fill="#6fb73d"/>
    </svg>

    <div class="brand">
      <span class="brand-dot"></span>
      <span class="brand-name">Greenleaf Hair Studios</span>
    </div>

    <p class="web">www.greenleafhairstudios.com.au</p>
  </section>

</main>
</body>
</html>
```